Tressvane hair oil bottle & packaging (Instagrammable)

I'm a blogger/social media influencer and I'm launching my own hair oil that I created myself. The hair oil is something I've used fora a long time and it makes your hair grow like there's no tomorrow!

I'm looking for a feminine and minimalistic bottle for the hair oil and also a nice packaging for the bottle. Please have a look at my Instagram account (@minaveltroo), I'd love if the product design and color scheme would be inspired by my Instagram feed. I'm looking for a design that would look very 'Instagrammable'

Product name: Tressvane
Bottle size: 100ml

Thank you xx

Target Market(s)

Females

Requirements
Must have
• According to the law this has to be marked on the packaging and on the bottle:
• Amount: 100ml
• Marked on the packaging:
• Ingredients: Burdock root oil, Grapeseed oil, Organic castor oil (maybe somehow draw attention to the fact that it's organic when designing the bottle & packaging), peppermint oil, Lavender oil, Cedarwood oil, Rosemary oil
Nice to have
• I added some photos of Ai Wenna packaging - I absolutely love it! The colour is exactly what I have in mind (also if you check my Instagram it's kind of my 'feed colour' - I'd be happy if the packaging would look something like that. The Ai Wenna packaging is exactly what I meant by 'Instagrammable'.
• Also - if we go for something like this, we could write Glow up! on the inside (so you see that when opening the packaging) or feel free to come up with something yourself, just bear in mind it's a hair oil that promotes hair growth

```html
<!DOCTYPE html>
<html lang="en">
<head>
<meta charset="utf-8">
<title>Tressvane Hair Growth Oil – Packaging</title>
<link href="https://fonts.googleapis.com/css2?family=Oswald:wght@400;500&family=Great+Vibes&family=Mrs+Saint+Delafield&display=swap" rel="stylesheet">
<style>
  :root {
    --paper: #fbf7f6;
    --blush: #f6d3d4;
    --blush-deep: #f2c9ca;
    --label: #f7d9d8;
    --rose-gold: #c89b86;
    --rose-gold-light: #e2bfae;
    --ink: #1d1a1a;
    --leaf-dark: #1f6b4f;
    --leaf-mid: #3f8f5e;
    --leaf-light: #7fb76a;
    --glass: #f4f2ec;
    --cap: #d9dadb;
  }
  * { box-sizing: border-box; margin: 0; padding: 0; }
  html, body { width: 845px; height: 1200px; overflow: hidden; background: var(--paper); }
  .canvas { position: relative; width: 845px; height: 1200px; background: var(--paper); }

  .box-face {
    position: absolute;
    box-shadow: 0 6px 14px rgba(120, 90, 90, 0.18);
  }
  .palm-print {
    position: absolute; inset: 0;
    background:
      radial-gradient(circle at 25% 20%, var(--leaf-light) 0 8%, transparent 22%),
      radial-gradient(circle at 75% 80%, var(--leaf-light) 0 6%, transparent 20%),
      linear-gradient(135deg, var(--leaf-dark) 0%, var(--leaf-mid) 45%, var(--blush) 50%, var(--leaf-mid) 55%, var(--leaf-dark) 100%);
  }
  .box-front { left: 68px; top: 52px; width: 324px; height: 472px; }
  .box-back  { left: 464px; top: 52px; width: 324px; height: 472px; }

  .label {
    position: absolute; left: 58px; top: 216px; width: 208px; height: 100px;
    background: var(--label);
    border: 2px solid var(--rose-gold-light);
    text-align: center;
    font-family: 'Oswald', sans-serif;
  }
  .brand-name {
    color: var(--rose-gold);
    font-weight: 500;
    letter-spacing: 1px;
    text-transform: uppercase;
  }
  .label-front .brand-name { font-size: 31px; margin-top: 24px; line-height: 1; }
  .volume { font-size: 7px; color: var(--ink); margin-top: 10px; letter-spacing: 0.5px; }

  .label-back .brand-name { font-size: 19px; margin-top: 8px; line-height: 1; }
  .product-type { font-size: 6px; color: var(--ink); margin-top: 5px; letter-spacing: 0.4px; }
  .ingredients { font-size: 5.6px; color: var(--ink); margin: 6px 10px 0; line-height: 1.6; letter-spacing: 0.2px; }
  .origin { font-size: 4.6px; color: var(--ink); margin-top: 4px; letter-spacing: 0.3px; }

  .inner-lid  { left: 68px; top: 612px; width: 336px; height: 508px; background: var(--blush); }
  .inner-spine { position: absolute; left: 404px; top: 612px; width: 60px; height: 508px; background: var(--blush-deep); }
  .inner-tray { left: 464px; top: 612px; width: 324px; height: 508px; background: var(--blush); }

  .greeting {
    position: absolute; left: 44px; top: 200px;
    font-family: 'Great Vibes', cursive;
    font-size: 46px; color: var(--rose-gold);
    transform: rotate(-4deg);
  }
  .sign-off {
    position: absolute; left: 196px; top: 272px;
    font-family: 'Mrs Saint Delafield', cursive;
    font-size: 24px; color: var(--ink);
  }

  .bottle {
    position: absolute; left: 36px; top: 28px; width: 140px; height: 248px;
  }
  .bottle-cap {
    position: absolute; left: 38px; top: 0; width: 64px; height: 58px;
    border-radius: 8px 8px 2px 2px;
    background: linear-gradient(90deg, #bfc0c2, var(--cap) 40%, #f3f3f3 60%, #c4c5c7);
  }
  .bottle-glass {
    position: absolute; left: 0; top: 58px; width: 140px; height: 190px;
    border-radius: 6px;
    background: linear-gradient(90deg, #e6e3dc, var(--glass) 25%, #ffffff 55%, #e9e6df);
    box-shadow: inset 0 0 0 2px rgba(200, 195, 185, 0.5);
  }
  .bottle-label {
    position: absolute; left: 28px; top: 96px; width: 84px; height: 70px;
    background: var(--label);
    border: 1.5px solid var(--rose-gold-light);
    text-align: center;
    font-family: 'Oswald', sans-serif;
  }
  .bottle-label .brand-name { font-size: 15px; margin-top: 20px; line-height: 1; }
  .bottle-label .volume { font-size: 4.5px; margin-top: 10px; }
</style>
</head>
<body>
<main class="canvas">

  <section class="box-face box-front">
    <div class="palm-print" role="img" aria-label="Watercolour tropical palm and monstera leaf pattern on blush pink"></div>
    <div class="label label-front">
      <p class="brand-name">Tressvane</p>
      <p class="volume">100 ML</p>
    </div>
  </section>

  <section class="box-face box-back">
    <div class="palm-print" role="img" aria-label="Watercolour tropical palm and monstera leaf pattern on blush pink"></div>
    <div class="label label-back">
      <p class="brand-name">Tressvane</p>
      <p class="product-type">HAIR GROWTH OIL</p>
      <p class="ingredients">INGREDIENTS: BURDOCK ROOT OIL, GRAPESEED OIL, ORGANIC CASTOR OIL, PEPPERMINT OIL, LAVENDER OIL, CEDARWOOD OIL, ROSEMARY OIL</p>
      <p class="origin">MADE IN AUSTRALIA</p>
    </div>
  </section>

  <section class="box-face inner-lid">
    <p class="greeting">Glow up!</p>
    <p class="sign-off">xx Mina</p>
  </section>

  <div class="inner-spine"></div>

  <section class="box-face inner-tray">
    <div class="bottle" role="img" aria-label="Clear square glass bottle with brushed silver cap">
      <div class="bottle-cap"></div>
      <div class="bottle-glass"></div>
      <div class="bottle-label">
        <p class="brand-name">Tressvane</p>
        <p class="volume">100 ML</p>
      </div>
    </div>
  </section>

</main>
</body>
</html>
```